Motivational Poster Design Project

I would like to create a poster with some of my favorite quotes to hang in my office. I did a similar project in 2012 and I've uploaded the top 2 designs so you can get a better idea of what I'm looking for. I will provide feedback on your design within 24 hours of receiving it.

The poster must contain the following quotes:

"You’re only given a little spark of madness. You mustn’t lose it.”
- Dorian Halbrook

“The most contrarian thing of all is not to oppose the crowd but to think for yourself.”
- Marcus Vell

"I constantly see people rise in life who are not the smartest, sometimes not even the most diligent, but they are learning machines. They go to bed every night a little wiser than they were when they got up and boy does that help, particularly when you have a long run ahead of you."
- Walter Brisco

“In theory, there’s no difference between theory and practice. But, in practice, there is.”
- Piet R. K. Ter Wolvenkamp

"At the end of the day, a reactionary life is a normal life. One thing is consistent in every remarkable person: they decide to do something remarkable. Don’t let the world choose who you become."
- Ravindra Kolpe

“It usually takes 3-4 months to try enough that you can do a proper 80/20 analysis, then two months to design systems to scale what *is* working.”
-Gus Ambery

“Authority is 20 percent given, 80 percent taken.”
- Harold Quimsby

“Your actions are consistent with the way the world occurs to you.”
- Anselm Grottke

Project Deadline Extended
Reason: I am going to be travelling with no access to internet until January 5th, 2015. I am extending the project deadline until 12/31/14 and I'll make a final decision during the 1st week of January.

Target Market(s)

Personal Project

Industry/Entity Type

Learning

Requirements
Must have
• The poster will be 24" high x 36" long and printed on canvas, so the image you create needs to have a resolution of at least 2700 x 3900.
Nice to have
• I don't have an exact vision for how the poster should look, so I am totally open to you using your creativity to develop, arrange and present the content as you'd like.
• That said, I would like an image (photo or posterized image) of the person being quoted along with each quote. I do not have specific images that I would like you to use, so you will need to find the images on your own. The images don't need to be perfect... I am more interested in the poster relating the essence of the quotes and the people being quoted than I am in perfect photographic images of the people being quoted.

```html
<!DOCTYPE html>
<html lang="en">
<head>
<meta charset="utf-8">
<title>Quotes Poster</title>
<link href="https://fonts.googleapis.com/css2?family=Alegreya+Sans:wght@300;400&family=Yellowtail&display=swap" rel="stylesheet">
<style>
  :root {
    --violet-deep: #4e1166;
    --violet: #7d2790;
    --rose: #c15f86;
    --amber: #e9973f;
    --gold: #f2b458;
    --sand: #f5c987;
    --quote-ink: #fff7ee;
    --name-cool: #f1e6f7;
    --name-warm: #fff1dc;
    --name-shadow-cool: #2b0638;
    --name-shadow-warm: #8a4a12;
    --panel-cool: rgba(40, 0, 60, 0.22);
    --panel-warm: rgba(255, 230, 190, 0.12);
  }
  * { margin: 0; padding: 0; box-sizing: border-box; }
  html, body { width: 836px; height: 1200px; overflow: hidden; }
  body {
    position: relative;
    font-family: "Alegreya Sans", sans-serif;
    background:
      radial-gradient(ellipse 260px 600px at 420px 600px, rgba(255, 200, 200, 0.35), transparent 70%),
      radial-gradient(ellipse 300px 300px at 640px 160px, rgba(255, 240, 200, 0.35), transparent 70%),
      linear-gradient(90deg, var(--violet-deep) 0%, var(--violet) 26%, var(--rose) 46%, var(--amber) 58%, var(--gold) 82%, var(--sand) 100%);
  }
  .poster { position: absolute; inset: 0; }

  .panel {
    position: absolute;
    width: 405px;
    height: 240px;
    padding: 22px 14px 12px;
    display: flex;
    flex-direction: column;
    justify-content: space-between;
    color: var(--quote-ink);
    font-size: 18px;
    line-height: 1.2;
    font-weight: 300;
  }
  .panel--cool { left: 0; background: var(--panel-cool); }
  .panel--warm { left: 431px; background: var(--panel-warm); }
  .panel--right-aligned { text-align: right; }
  .panel--flow { justify-content: flex-start; gap: 0; }
  .panel--flow .line { line-height: 1.3; }

  .line { display: block; }
  .line--indent { padding-left: 106px; }
  .line--gap { margin-top: 22px; }

  .portrait {
    position: absolute;
    width: 84px;
    height: 96px;
    border-radius: 50%;
  }
  .portrait--cool {
    background: radial-gradient(ellipse at 50% 45%, #e5b4ee 0%, #9c4bb2 45%, rgba(90, 20, 110, 0) 72%);
  }
  .portrait--warm {
    background: radial-gradient(ellipse at 50% 45%, #f4d2a3 0%, #c9833e 45%, rgba(220, 140, 60, 0) 72%);
  }

  .name {
    position: absolute;
    font-family: "Yellowtail", cursive;
    font-size: 30px;
    letter-spacing: 0.5px;
    line-height: 1;
    white-space: nowrap;
  }
  .name--cool {
    color: var(--name-cool);
    text-shadow: 1px 1px 0 var(--name-shadow-cool), 2px 2px 3px rgba(20, 0, 30, 0.6);
  }
  .name--warm {
    color: var(--name-warm);
    text-shadow: 1px 1px 0 var(--name-shadow-warm), 2px 2px 3px rgba(90, 40, 0, 0.5);
  }
</style>
</head>
<body>
<main class="poster">

  <!-- Row 1 -->
  <section class="panel panel--cool panel--right-aligned" style="top:10px;height:230px;padding:18px 8px 6px;">
    <span class="line">“You’re only given a little</span>
    <span class="line">spark of madness.</span>
    <span class="line">You MUSTN’T lose it.”</span>
  </section>
  <div class="portrait portrait--cool" style="left:28px;top:14px;" role="img" aria-label="Portrait of Dorian Halbrook"></div>
  <p class="name name--cool" style="left:122px;top:243px;">Dorian Halbrook R.I.P</p>

  <section class="panel panel--warm" style="top:10px;height:230px;padding:18px 8px 6px;">
    <span class="line">“The most contrarian thing of all</span>
    <span class="line">is not to oppose the crowd</span>
    <span class="line">but to think for yourself.”</span>
  </section>
  <div class="portrait portrait--warm" style="left:728px;top:12px;" role="img" aria-label="Portrait of Marcus Vell"></div>
  <p class="name name--warm" style="left:436px;top:243px;">Marcus Vell</p>

  <!-- Row 2 -->
  <section class="panel panel--cool" style="top:298px;padding:14px 16px 8px;">
    <span class="line">"At the end of the day, a reactionary life</span>
    <span class="line">is a normal life. One thing is consistent</span>
    <span class="line">in every remarkable person: they decide</span>
    <span class="line">to do something remarkable. Don’t let the world</span>
    <span class="line">choose who you become."</span>
  </section>
  <div class="portrait portrait--cool" style="left:322px;top:312px;" role="img" aria-label="Portrait of Ravindra Kolpe"></div>
  <p class="name name--cool" style="left:18px;top:537px;">Ravindra Kolpe</p>

  <section class="panel panel--warm panel--flow" style="top:298px;width:405px;padding:14px 6px 8px 2px;font-size:17.5px;">
    <span class="line line--indent">"I constantly see people rise in life who</span>
    <span class="line line--indent">are not the smartest, sometimes not</span>
    <span class="line line--indent">even the most diligent, but they are</span>
    <span class="line">learning machines. They go to bed every night a</span>
    <span class="line">little wiser than they were when they got up and boy</span>
    <span class="line">does that help, particularly when you have a long</span>
    <span class="line">run ahead of you."</span>
  </section>
  <div class="portrait portrait--warm" style="left:446px;top:310px;" role="img" aria-label="Portrait of Walter Brisco"></div>
  <p class="name name--warm" style="right:20px;top:540px;font-size:27px;">Walter Brisco</p>

  <!-- Row 3 -->
  <section class="panel panel--cool panel--right-aligned" style="top:598px;height:232px;padding:16px 14px 6px;">
    <span class="line">“It usually takes 3-4 months to try</span>
    <span class="line">enough that you can do a proper</span>
    <span class="line">80/20 analysis, then two months</span>
    <span class="line">to design systems to scale what *is* working.”</span>
  </section>
  <div class="portrait portrait--cool" style="left:38px;top:604px;" role="img" aria-label="Portrait of Gus Ambery"></div>
  <p class="name name--cool" style="right:436px;top:836px;">Gus Ambery</p>

  <section class="panel panel--warm" style="top:598px;height:232px;padding:16px 8px 6px;">
    <span class="line">“In theory, there’s no difference</span>
    <span class="line">between theory and practice.</span>
    <span class="line">But, in practice, there is.”</span>
  </section>
  <div class="portrait portrait--warm" style="left:728px;top:610px;" role="img" aria-label="Portrait of Piet R. K. Ter Wolvenkamp"></div>
  <p class="name name--warm" style="left:436px;top:836px;font-size:27px;">Piet R. K. Ter Wolvenkamp R.I.P</p>

  <!-- Row 4 -->
  <section class="panel panel--cool" style="top:892px;height:190px;padding:14px 18px 6px;">
    <span class="line">“Authority is 20 percent given,</span>
    <span class="line">80 percent taken.”</span>
  </section>
  <div class="portrait portrait--cool" style="left:318px;top:902px;" role="img" aria-label="Portrait of Harold Quimsby"></div>
  <p class="name name--cool" style="left:18px;top:1134px;">Harold Quimsby</p>

  <section class="panel panel--warm panel--right-aligned" style="top:892px;height:190px;padding:14px 14px 6px;">
    <span class="line">“Your actions are consistent with</span>
    <span class="line">the way the world occurs to you.”</span>
  </section>
  <div class="portrait portrait--warm" style="left:438px;top:902px;" role="img" aria-label="Portrait of Anselm Grottke"></div>
  <p class="name name--warm" style="right:22px;top:1134px;">Anselm Grottke</p>

</main>
</body>
</html>
```